Morden, Creative, Unique, Independent Wine Shop

1. We are a brand new wine shop located in Melbourne Australia, we have our logo already, simply use the logo to design a business card.
2. I have uploaded our logo in two versions, with or without shadow, any of them is acceptable.
3. Make it as creative and unique as possible, no limitation of shape, color combination, geometry pattern, fonts, composing etc.
3. Info on the card:
- Brambleford Wine Cellar (Not very necessary if logo is obviously shown)
- 42 Ferncastle Steet, Hampton, Victoria, Australia 3188
- +61 3 9018 4637
- www.bramblefordwinecellar.com.au
- bramblefordwinecellar@mailvista.com
- Additional icons: Google, Instagram, Facebook, Twitter
4. Once again, forget it is a commercial card, make it special.

```html
<!DOCTYPE html>
<html lang="en">
<head>
<meta charset="utf-8">
<title>Brambleford Wine Cellar – Business Card</title>
<link href="https://fonts.googleapis.com/css2?family=Lato:wght@400;700&display=swap" rel="stylesheet">
<style>
  :root {
    --page-bg: #d9d2ca;
    --card-frost: #ece5dd;
    --wine-deep: #861a2a;
    --wine-bright: #a72739;
    --curve-shadow: #2a2324;
    --name-ink: #3a2a2c;
    --info-ink: #f3dde0;
    --brand-ink: #7a1c26;
  }
  * { margin: 0; padding: 0; box-sizing: border-box; }
  html, body {
    width: 1200px; height: 1047px; overflow: hidden;
    background: var(--page-bg);
    font-family: "Lato", sans-serif;
  }
  .card {
    position: absolute; left: 120px; top: 261px;
    width: 960px; height: 525px;
    border-radius: 22px; overflow: hidden;
    background: var(--card-frost);
    box-shadow: 0 10px 30px rgba(60, 40, 40, 0.18);
  }
  .card-art { position: absolute; inset: 0; }
  .holder-name {
    position: absolute; left: 38px; top: 68px;
    font-size: 38px; font-weight: 700; letter-spacing: 0.5px;
    color: var(--name-ink);
  }
  .holder-role {
    position: absolute; left: 38px; top: 116px;
    font-size: 24px; color: var(--info-ink);
  }
  .address {
    position: absolute; left: 38px; top: 242px;
    font-size: 23px; line-height: 31px; color: var(--info-ink);
  }
  .contact-list { position: absolute; left: 38px; top: 326px; list-style: none; }
  .contact-item {
    display: flex; align-items: center; height: 38px;
    font-size: 23px; color: var(--info-ink);
  }
  .contact-icon { width: 22px; height: 22px; margin-right: 16px; flex: none; }
  .social-row { position: absolute; left: 178px; top: 470px; display: flex; gap: 15px; }
  .social-dot {
    width: 27px; height: 27px; border-radius: 50%;
    border: 1.5px solid var(--info-ink);
  }
  .brand {
    position: absolute; left: 560px; top: 222px;
    display: flex; align-items: center; gap: 22px;
  }
  .brand-mark {
    width: 56px; height: 56px; border-radius: 50%;
    background: var(--brand-ink);
  }
  .brand-name {
    font-size: 28px; font-weight: 400; letter-spacing: 2px; line-height: 34px;
    color: var(--brand-ink); text-transform: uppercase;
  }
</style>
</head>
<body>
  <div class="card">
    <svg class="card-art" width="960" height="525" viewBox="0 0 960 525" aria-hidden="true">
      <defs>
        <linearGradient id="wineFill" x1="0" y1="0" x2="1" y2="1">
          <stop offset="0" stop-color="var(--wine-deep)"/>
          <stop offset="0.55" stop-color="var(--wine-bright)"/>
          <stop offset="1" stop-color="var(--wine-deep)"/>
        </linearGradient>
      </defs>
      <path class="curve-shadow" d="M540 90 C470 240 480 410 565 525 H540 C470 410 455 240 540 90 Z" fill="var(--curve-shadow)"/>
      <path class="wine-panel" d="M0 0 H556 C470 150 440 330 540 525 H0 Z" fill="url(#wineFill)"/>
    </svg>

    <div class="holder-name">DANIEL HARTLEY</div>
    <div class="holder-role">Founder &amp;&nbsp; CEO</div>

    <div class="address">42 Ferncastle Steet, Hampton,<br>Victoria, Australia 3188</div>

    <ul class="contact-list">
      <li class="contact-item">
        <svg class="contact-icon" viewBox="0 0 24 24" fill="none" stroke="var(--name-ink)" stroke-width="2" stroke-linecap="round" stroke-linejoin="round"><path d="M5 3h4l2 5-2.5 1.5a11 11 0 0 0 6 6L16 13l5 2v4a2 2 0 0 1-2 2A16 16 0 0 1 3 5a2 2 0 0 1 2-2z"/></svg>
        +61 3 9018 4637
      </li>
      <li class="contact-item">
        <svg class="contact-icon" viewBox="0 0 24 24" fill="none" stroke="var(--name-ink)" stroke-width="2" stroke-linejoin="round"><rect x="2" y="5" width="20" height="14"/><path d="M2 5l10 8 10-8"/></svg>
        bramblefordwinecellar@mailvista.com
      </li>
      <li class="contact-item">
        <svg class="contact-icon" viewBox="0 0 24 24" fill="none" stroke="var(--name-ink)" stroke-width="2"><circle cx="12" cy="12" r="9"/><path d="M3 12h18M12 3c3 3 3 15 0 18M12 3c-3 3-3 15 0 18"/></svg>
        www.bramblefordwinecellar.com.au
      </li>
    </ul>

    <div class="social-row">
      <span class="social-dot"></span>
      <span class="social-dot"></span>
      <span class="social-dot"></span>
    </div>

    <div class="brand">
      <span class="brand-mark"></span>
      <div class="brand-name">Brambleford<br>Wine Cellar</div>
    </div>
  </div>
</body>
</html>
```